Cleaning/ butler service flyer design

We need a flyer that will be distributed through letter boxes for a small company based in Leamington Spa, called Rodrigo and Teodoro - We offer an in depth cleaning service as a one off, or regular weekly cleaning to suit the client. Rodrigo and Teodoro are experienced in hotel housekeeper services, and know the difference between what looks clean and what really is clean. We would like the designs to include green and blue colours. The flyer should also have a hint of humour but communicate trust and flexibility.

I the flyer to capitalise on the personality of these two Spanish guys doing a cleaning service.
- Logo: Use words – Rodrigo & Teodoro
o In Century Gothic Bold font
o Use a hoover to create the ‘&’ giving it the quirky logo

Rodriego & Teodoro
Cleaning at your service

I like the use of the strap line “ we know the difference between what looks clean and what really is clean”

We will provide a phone number and an email address as contact details which should appear at the bottom of the flyer.

Blue and Green colours to be used

I want the flyer to convey the fact that we don’t take our selves too seriously hence the need for humour (a bit like Ignacio in crooked gables), but the Home Cleaning Service is the main service that is offered so please use images that convey ‘Homey’ feelings.

Target Market(s)

Adults aged 36 - 55, men and women who live alone and work long hours and the last thing they want to do is clean their house on a weekend. Families with kids and or pets

Industry/Entity Type

Cleaning Service

Font styles to use
Other font styles liked:
• Century Gothic

Colors
0355a3
00a88f

Requirements
Must have
• I want to place 3 testimonials to evoke the service

```html
<!DOCTYPE html>
<html lang="en">
<head>
<meta charset="utf-8">
<title>Rodrigo &amp; Teodoro – Cleaning at your service</title>
<link rel="stylesheet" href="https://fonts.googleapis.com/css2?family=Montserrat:ital,wght@0,400;0,700;0,800;1,700;1,800&family=Roboto+Condensed:wght@400&family=Dancing+Script:wght@700&display=swap">
<style>
  :root {
    --brand-blue: #0355a3;
    --brand-green: #00a88f;
    --bubble-green: #12b497;
    --ink-white: #ffffff;
    --page: #ffffff;
    --art-light: #e7eef7;
    --art-mid: #b9d3ea;
  }
  * { box-sizing: border-box; margin: 0; padding: 0; }
  html, body { width: 929px; height: 1200px; overflow: hidden; background: var(--page); }
  .flyer {
    position: relative; width: 929px; height: 1200px; overflow: hidden;
    background: var(--page); font-family: "Montserrat", sans-serif;
  }
  .header-band { position: absolute; left: 0; top: 0; width: 929px; height: 190px; }
  .strapline {
    position: absolute; left: 0; top: 36px; width: 929px; text-align: center;
    color: var(--ink-white); font-weight: 700; white-space: nowrap;
  }
  .strapline-lead { font-size: 29px; line-height: 1.2; }
  .strapline-main { font-size: 31px; font-style: italic; font-weight: 800; line-height: 1.2; margin-top: 10px; letter-spacing: -0.3px; }

  .testimonial {
    position: absolute; left: 60px; width: 290px;
    background: var(--bubble-green); color: var(--ink-white);
    border-radius: 30px; padding: 18px 24px;
    font-family: "Roboto Condensed", sans-serif;
    font-size: 17px; line-height: 1.28; text-align: center;
  }
  .testimonial::after {
    content: ""; position: absolute; right: -16px; top: 50%;
    border-left: 22px solid var(--bubble-green);
    border-top: 14px solid transparent; border-bottom: 14px solid transparent;
    transform: translateY(-50%);
  }
  .testimonial cite { font-style: normal; }
  .t-one { top: 196px; }
  .t-two { top: 408px; }
  .t-three { top: 528px; }

  .brand-name {
    position: absolute; left: 440px; top: 198px; width: 490px; text-align: center;
    color: var(--brand-blue); font-weight: 800; font-size: 62px; line-height: 1.0;
    letter-spacing: 1px;
  }
  .tagline {
    position: absolute; left: 420px; top: 390px; width: 509px; text-align: center;
    font-family: "Dancing Script", cursive; color: var(--brand-green);
    font-size: 46px; font-weight: 700; line-height: 1.2;
  }
  .experience {
    position: absolute; left: 400px; top: 466px; width: 529px; text-align: center;
    color: var(--brand-blue); font-weight: 800; font-size: 20px; line-height: 1.3;
  }
  .kid-art {
    position: absolute; left: 620px; top: 590px; width: 280px; height: 420px;
    border-radius: 40px;
    background: radial-gradient(ellipse at 55% 55%, var(--art-mid), var(--art-light) 70%, var(--page));
  }
  .speech {
    position: absolute; left: 484px; top: 650px; width: 178px; height: 108px;
    border: 4px solid var(--brand-blue); border-radius: 50%; background: var(--page);
    display: flex; align-items: center; justify-content: center; text-align: center;
    color: var(--brand-blue); font-weight: 700; font-size: 24px; line-height: 1.15;
  }
  .services { position: absolute; left: 14px; top: 758px; width: 720px; height: 258px; }
  .services-list {
    position: absolute; left: 14px; top: 778px; width: 720px; text-align: center;
    color: var(--ink-white); font-size: 28px; line-height: 1.36; list-style: none;
  }
  .call-to-action {
    position: absolute; left: 0; top: 1058px; width: 929px; text-align: center;
    color: var(--brand-blue); font-style: italic; font-weight: 800; font-size: 29px;
    white-space: nowrap;
  }
  .contact {
    position: absolute; left: 0; top: 1128px; width: 929px;
    display: flex; justify-content: center; gap: 90px;
    color: var(--brand-blue); font-weight: 700; font-size: 27px;
  }
  .contact-item { display: flex; align-items: center; gap: 14px; }
</style>
</head>
<body>
<main class="flyer">
  <svg class="header-band" viewBox="0 0 929 190" aria-hidden="true">
    <path d="M0 0 H929 V134 Q464 222 0 134 Z" fill="var(--brand-blue)"/>
  </svg>
  <h1 class="strapline">
    <div class="strapline-lead">We know the difference between</div>
    <div class="strapline-main">what looks clean &amp; what really is clean...</div>
  </h1>

  <blockquote class="testimonial t-one">“We really struggled to find a reliable cleaning service that was consistent week in week out, these two Spanish guys turned up and have done and continue to do a really good job – Ole!” <cite>Harriet – Larchmere Avenue</cite></blockquote>
  <blockquote class="testimonial t-two">“They even texted me after to ask if I was happy with the service”<br><cite>Simon – Elmfield Gate</cite></blockquote>
  <blockquote class="testimonial t-three">“I suffer from dust allergies, so I can tell when a cleaner hasn’t been through, I’ve been through loads and I can tell you, these guys really do clean” <cite>Gareth – Brookhurst</cite></blockquote>

  <div class="brand-name">RODRIGO<br>&amp;<br>TEODORO</div>
  <p class="tagline">Cleaning at your service</p>
  <p class="experience">RODRIGO AND TEODORO ARE EXPERIENCED<br>IN HOTEL HOUSEKEEPER SERVICES</p>

  <div class="kid-art" role="img" aria-label="Illustration of a cross little girl leaning on a vacuum cleaner beside a mop bucket"></div>
  <div class="speech">“But mom!<br>It’s CLEAN!”</div>

  <svg class="services" viewBox="0 0 720 258" aria-hidden="true">
    <ellipse cx="360" cy="129" rx="358" ry="127" fill="var(--brand-blue)"/>
  </svg>
  <ul class="services-list">
    <li>In-depth cleaning</li>
    <li>Dog walking service available</li>
    <li>Additional services to assist</li>
    <li>in the smooth running of the household</li>
  </ul>

  <p class="call-to-action">Call today for our in depth cleaning service!</p>
  <div class="contact">
    <span class="contact-item">
      <svg width="32" height="24" viewBox="0 0 32 24" aria-hidden="true"><rect x="2" y="2" width="28" height="20" rx="2" fill="none" stroke="var(--brand-blue)" stroke-width="3"/><path d="M3 3 L16 14 L29 3" fill="none" stroke="var(--brand-blue)" stroke-width="3"/></svg>
      email@email.com
    </span>
    <span class="contact-item">
      <svg width="26" height="30" viewBox="0 0 26 30" aria-hidden="true"><path d="M6 2 L11 2 L13 9 L9 12 Q12 19 17 22 L20 18 L25 21 L24 27 Q22 29 18 28 Q4 22 2 7 Q2 3 6 2 Z" fill="var(--brand-blue)"/></svg>
      555.555.5555
    </span>
  </div>
</main>
</body>
</html>
```